Graphic Banner Design - 2.5' x 6' - High Tech Company

We are in need of a banner design for an outdoor sign that will be used at sponsorship events.

Size
2.5' x 6'

The company is a high tech company, and the design will be used for action sports events. So lining up to that would be good.

Tag line to be incorporated...
"Extreme IT Services for Extreme Needs."

Target Market(s)

Business Owners, Entrepreneurs, IT Professionals.

Industry/Entity Type

Information Technology

Logo Text

Vexlora

Colors

Designer to choose colors to be used in the design.

Requirements
Must have
• Must feel young and vibrant, fit in to an action sports event and just be out of this world awesome.
• In the world of the IT, we are the Zanverolli. Fast, Awesome, not necessarily cheap, but you know it will do what you want extremely well. Not for everyone, but always desired.

```html
<!DOCTYPE html>
<html lang="en">
<head>
<meta charset="utf-8">
<title>Extreme IT Services Banner</title>
<link rel="stylesheet" href="https://fonts.googleapis.com/css2?family=Graduate&display=swap">
<style>
  :root {
    --ink: #0b0d1e;
    --navy: #12195a;
    --royal: #2a3fe0;
    --sky: #3f8dff;
    --crimson: #e8213c;
    --magenta: #d4209a;
    --mint: #2df5a0;
    --violet: #5a1fb0;
    --tag-fill: #f2f0ea;
    --tag-stroke: #111111;
  }
  html, body {
    margin: 0;
    padding: 0;
    overflow: hidden;
    background: var(--ink);
  }
  .banner {
    position: relative;
    width: 1200px;
    height: 500px;
    overflow: hidden;
    background: var(--ink);
  }
  .arena-photo {
    position: absolute;
    inset: 0;
    background:
      radial-gradient(ellipse 90px 200px at 600px 200px, rgba(210,210,225,0.55), transparent 70%),
      radial-gradient(ellipse 260px 120px at 380px 80px, rgba(255,40,90,0.75), transparent 70%),
      radial-gradient(ellipse 300px 140px at 820px 90px, rgba(60,150,255,0.8), transparent 70%),
      radial-gradient(ellipse 200px 80px at 560px 300px, rgba(230,230,255,0.35), transparent 70%),
      linear-gradient(180deg, #3a2a8a 0%, #4a3fb0 30%, #3a2a70 55%, #7a1a4a 72%, #1a1030 88%, #0b0d1e 100%);
  }
  .edge-bands {
    position: absolute;
    inset: 0;
    width: 1200px;
    height: 500px;
  }
  .tagline {
    position: absolute;
    left: 624px;
    top: 372px;
    transform: translateX(-50%);
    margin: 0;
    font-family: "Graduate", serif;
    font-weight: 400;
    font-size: 34px;
    line-height: 58px;
    letter-spacing: 1px;
    text-align: center;
    white-space: nowrap;
    color: var(--tag-fill);
    -webkit-text-stroke: 1.5px var(--tag-stroke);
    paint-order: stroke fill;
    text-shadow: 0 0 4px var(--tag-stroke), 0 0 2px var(--tag-stroke);
  }
</style>
</head>
<body>
  <div class="banner">
    <div class="arena-photo" role="img" aria-label="Photo of a lit esports arena stage with a silver trophy cup in front of a crowd"></div>

    <svg class="edge-bands" viewBox="0 0 1200 500" aria-hidden="true">
      <!-- left chevrons pointing right -->
      <g class="chevrons-left">
        <polygon points="0,0 190,0 368,195 300,500 0,500" fill="var(--navy)"/>
        <polygon points="0,0 150,0 330,195 260,500 0,500" fill="var(--royal)"/>
        <polygon points="80,0 140,0 300,190 240,500 180,500 240,190" fill="var(--crimson)"/>
        <polygon points="40,0 80,0 240,190 180,500 140,500 200,190" fill="var(--sky)"/>
        <polygon points="0,60 150,190 100,500 60,500 110,195 0,100" fill="var(--magenta)"/>
        <polygon points="0,140 95,200 60,500 30,500 65,205 0,170" fill="var(--mint)"/>
        <polygon points="0,170 65,205 30,500 0,500" fill="var(--navy)"/>
        <polygon points="200,0 220,0 368,195 352,195" fill="var(--mint)"/>
        <polygon points="352,195 368,195 300,500 284,500" fill="var(--sky)"/>
      </g>
      <!-- right chevrons pointing left -->
      <g class="chevrons-right">
        <polygon points="944,0 1200,0 1200,500 900,500 848,248" fill="var(--navy)"/>
        <polygon points="990,0 1200,0 1200,500 950,500 890,250" fill="var(--violet)"/>
        <rect x="1000" y="105" width="200" height="10" fill="var(--crimson)"/>
        <rect x="950" y="130" width="250" height="12" fill="var(--mint)"/>
        <polygon points="900,165 1200,165 1200,195 880,195" fill="var(--royal)"/>
        <rect x="860" y="215" width="340" height="12" fill="var(--magenta)"/>
        <rect x="880" y="240" width="320" height="8" fill="var(--sky)"/>
        <polygon points="870,262 1200,262 1200,290 900,290" fill="var(--crimson)"/>
        <rect x="920" y="310" width="280" height="10" fill="var(--mint)"/>
        <polygon points="940,340 1200,340 1200,380 960,380" fill="var(--royal)"/>
        <rect x="960" y="400" width="240" height="10" fill="var(--magenta)"/>
        <rect x="920" y="440" width="280" height="12" fill="var(--sky)"/>
        <polygon points="944,0 960,0 864,248 848,248" fill="var(--mint)"/>
        <polygon points="848,248 864,248 916,500 900,500" fill="var(--sky)"/>
      </g>
    </svg>

    <p class="tagline">EXTREME IT SERVICES<br>FOR EXTREME NEEDS.</p>
  </div>
</body>
</html>
```